Relaunch Instagram Posts Design

We want to give you a better understanding about the expected outcome of this task, and give you a little bit of a background that should help you throughout.
We already have social media accounts, they aren’t active and the posts are outdated. We just finished our rebranding exercise, and accordingly we are planning to have a re-launch where we communicate our new identity, and rebuild our online existence, to enhance our social media presence and engagement.
Thus, we want to formulate the style of posting from the beginning, so that it reflects the identity overall and we can move forward with in a consistent manner.

Find attached details. We will share other files later. You need to read the attachment in the project to understand the requirement. Also, you should use the attached images in the project. You should also use products images from our website...www.bloomvelara.com
Our Primary color is #5725A9, PURPLE (based on color HEX Code)
Our Secondary colors #7C50BE, #A17BD3, #C5A6E8, #EAD1FD
Also, this secondary colors can be used #2B9348, #55A630, #80B918, #AACC00

Target Market(s)

Gift-givers who would like to bring a gift of value and meaning, representing the occasion

Industry/Entity Type

Flowers

Colors

Designer to choose colors to be used in the design.

Requirements
Must have
• Image based posts with little graphics + typography-based posts.... hammer on the emotional aspect, focusing on special moments such as using images related nice moments
Nice to have
• A full overview as in the brief (with all 21 posts), to give the sense of the design direction for us to know if it fits our new brand vision or not.
Should not have
• A typical commercial design direction that focuses so much on direct product communication. This definitely will be there, but we want this to be integrated with the other aspects.

```html
<!DOCTYPE html>
<html lang="en">
<head>
<meta charset="utf-8">
<title>Bloom Velara – Relaunch Posts</title>
<link href="https://fonts.googleapis.com/css2?family=Allura&family=Poppins:wght@400;500;600;800&display=swap" rel="stylesheet">
<style>
  :root{
    --purple:#5725a9;
    --purple-mid:#7c50be;
    --lavender:#e6c8f2;
    --gold:#d9b25a;
    --yellow:#f2d417;
    --green:#55a630;
    --green-light:#80b918;
    --white:#ffffff;
    --canvas:#e4e4e6;
  }
  *{box-sizing:border-box;margin:0;padding:0}
  html,body{width:1200px;height:2400px;overflow:hidden}
  body{background:var(--canvas);position:relative;font-family:'Poppins',sans-serif}
  .abs{position:absolute}

  /* ---------- Quote post ---------- */
  .quote-post{left:290px;top:485px;width:620px;height:620px;overflow:hidden;
    background:linear-gradient(160deg,#3a3a3a 0%,#6f6f6f 35%,#a9a9a9 60%,#6a6a6a 100%);
    box-shadow:0 6px 18px rgba(0,0,0,.25)}
  .quote-post .scene{inset:0;background:
      radial-gradient(ellipse 55% 40% at 20% 18%,#262626 0,transparent 70%),
      radial-gradient(ellipse 25% 60% at 88% 55%,#c9c9c9 0,transparent 70%),
      radial-gradient(ellipse 40% 20% at 50% 92%,#8a8a8a 0,transparent 70%)}
  .quote-post .couple{left:0;top:362px;width:170px;height:258px;
    background:
      radial-gradient(ellipse 45% 30% at 55% 25%,#d8b79a 0,transparent 75%),
      radial-gradient(ellipse 70% 55% at 45% 80%,#6f8fb8 0,transparent 80%),
      linear-gradient(180deg,rgba(160,150,140,.2),rgba(90,110,140,.6));
    border-radius:0 40px 0 0}
  .quote-box{left:96px;top:92px;width:415px;height:405px;background:var(--purple);
    border-radius:4px 8px 10px 4px}
  .quote-frame{left:0;top:0;width:620px;height:620px;pointer-events:none}
  .quote-script{left:96px;top:128px;width:415px;text-align:center;font-family:'Allura',cursive;
    color:var(--yellow);font-size:44px;line-height:44px;white-space:nowrap}
  .quote-body{left:96px;top:222px;width:415px;text-align:center;color:var(--white);
    font-size:25px;line-height:32px;font-weight:400;white-space:nowrap}
  .quote-orchid{left:220px;top:384px;width:165px;height:48px;
    background:radial-gradient(ellipse 50% 50% at 55% 50%,#e35fb0 0,#c2348f 35%,rgba(123,191,74,.7) 65%,transparent 100%)}
  .brand-mark{display:flex;align-items:center;gap:8px;font-family:'Poppins',sans-serif;
    font-weight:600;color:var(--purple);white-space:nowrap}
  .brand-mark .dot{border-radius:50%;background:var(--green)}
  .quote-post .brand-mark{left:415px;top:532px;font-size:22px;color:var(--white)}
  .quote-post .brand-mark .dot{width:20px;height:20px;background:var(--yellow)}

  /* ---------- Profile grid ---------- */
  .profile-grid{left:60px;top:1195px;width:1080px;height:720px;overflow:hidden;
    background:
      radial-gradient(circle at 15% 85%,#f7c9d8 0,transparent 35%),
      radial-gradient(circle at 92% 80%,#f9c6d3 0,transparent 30%),
      radial-gradient(circle at 50% 40%,#fff2ea 0,transparent 50%),
      linear-gradient(180deg,#fcf1e4 0%,#fbe6ea 55%,#f8dbe8 100%);
    box-shadow:0 6px 18px rgba(0,0,0,.2)}
  .lavender-panel{left:696px;top:0;width:384px;height:376px;
    background:linear-gradient(160deg,#f3d3f8 0%,var(--lavender) 60%,#dcb8ef 100%)}
  .gold-lines{left:0;top:0;width:1080px;height:720px}
  .script{font-family:'Allura',cursive;color:var(--purple);white-space:nowrap;text-align:center}

  .preserved-photo{left:65px;top:45px;width:205px;height:165px;
    background:
      radial-gradient(ellipse 28% 45% at 30% 50%,#b3242c 0,rgba(240,225,200,.9) 55%,transparent 100%),
      radial-gradient(ellipse 22% 38% at 75% 55%,#9c2a20 0,rgba(230,200,140,.9) 55%,transparent 100%)}
  .preserved-label{left:60px;top:222px;width:230px;font-size:40px}

  .grid-orchid{left:590px;top:0;width:165px;height:100px;
    background:radial-gradient(ellipse 50% 55% at 50% 30%,#e0559b 0,#f5a8c8 45%,transparent 100%)}
  .floral-lineart{left:530px;top:210px;width:170px;height:150px;
    background:radial-gradient(circle,#ecdcf6 0,transparent 70%)}
  .profile-grid .brand-mark{left:408px;top:142px;font-size:32px}
  .profile-grid .brand-mark .dot{width:32px;height:32px}

  .roses-photo{left:840px;top:35px;width:105px;height:85px;
    background:radial-gradient(ellipse 50% 45% at 50% 55%,#3a2f25 0,#caa040 45%,transparent 100%)}
  .roses-label{left:840px;top:118px;width:120px;font-size:46px}
  .domes-photo{left:818px;top:172px;width:160px;height:120px;
    background:radial-gradient(ellipse 50% 50% at 50% 50%,#cf1f2a 0,#e8a3aa 50%,transparent 100%)}
  .projects-label{left:755px;top:284px;width:290px;font-size:46px}

  .gifts-photo{left:120px;top:378px;width:130px;height:200px;
    background:
      radial-gradient(ellipse 50% 20% at 50% 12%,#d11f27 0,transparent 100%),
      radial-gradient(ellipse 40% 45% at 50% 65%,#1d1d1d 0,#3a3a3a 50%,transparent 100%)}
  .gifts-label{left:105px;top:590px;width:160px;font-size:34px;line-height:30px;white-space:normal}

  .mission-text{left:372px;top:415px;width:330px;text-align:center}
  .mission-text .green{font-family:'Allura',cursive;color:var(--green);font-size:48px;line-height:50px}
  .mission-text .white{font-family:'Allura',cursive;color:var(--white);font-size:48px;line-height:50px}
  .mission-text .yellow{font-family:'Allura',cursive;color:var(--yellow);font-size:48px;line-height:50px}
  .mission-text .tag{color:var(--white);font-size:19px;margin-top:6px}
  .gold-leaves{left:440px;top:630px;width:195px;height:80px;
    background:radial-gradient(ellipse 50% 70% at 50% 100%,#c99a52 0,#f2dcae 55%,transparent 100%)}

  .since{left:790px;top:440px;width:200px;text-align:center;font-weight:800}
  .since .label{font-size:15px;letter-spacing:6px;color:#333;font-weight:600}
  .since .num{font-size:86px;line-height:80px;letter-spacing:-2px}
  .since .top{color:var(--green-light)}
  .since .bottom{color:var(--purple)}
  .wreath{left:975px;top:430px;width:100px;height:250px;
    background:radial-gradient(ellipse 50% 50% at 50% 55%,#f5c04a 0,#f7e08a 35%,#f2b5b0 60%,transparent 100%)}
</style>
</head>
<body>

<!-- Quote post -->
<section class="abs quote-post" aria-label="Emotional quote post">
  <div class="abs scene" role="img" aria-label="Black and white garden photo with stone column"></div>
  <div class="abs quote-box"></div>
  <svg class="abs quote-frame" viewBox="0 0 620 620" fill="none" stroke="#fff" stroke-width="3">
    <polyline points="84,88 500,78 508,470 88,480 84,88"/>
    <polyline points="102,96 522,100 514,494 104,486"/>
  </svg>
  <div class="abs couple" role="img" aria-label="Photo of a couple embracing"></div>
  <p class="abs quote-script">Our hearts stay<br>connected to memories.</p>
  <p class="abs quote-body">No matter where life<br>takes us, we dont let go<br>of the special moments<br>and people shared with.</p>
  <div class="abs quote-orchid" role="img" aria-label="Pink orchid spray"></div>
  <div class="abs brand-mark"><span class="dot"></span>Bloom Velara</div>
</section>

<!-- Profile grid -->
<section class="abs profile-grid" aria-label="Profile grid of launch posts">
  <div class="abs lavender-panel" role="img" aria-label="Soft lavender rose background"></div>

  <svg class="abs gold-lines" viewBox="0 0 1080 720" fill="none" stroke="#d9b25a" stroke-width="2.5">
    <polyline points="180,20 337,20 337,180"/>
    <polyline points="22,180 22,335 180,335"/>
    <polyline points="540,22 690,22 690,180"/>
    <polyline points="382,180 382,330 540,330"/>
    <polyline points="398,188 398,318 540,318"/>
    <line x1="230" y1="330" x2="430" y2="245"/>
    <line x1="230" y1="330" x2="390" y2="470"/>
    <polygon points="160,380 280,450 280,590 160,660 40,590 40,450" stroke-width="2"/>
    <polygon points="170,390 290,470 270,610 150,650 50,580 60,440" stroke-width="1.5"/>
    <circle cx="537" cy="543" r="176" stroke-width="4"/>
    <circle cx="890" cy="545" r="132" stroke-width="2.5"/>
    <circle cx="890" cy="545" r="122" stroke-width="1.5"/>
  </svg>

  <div class="abs preserved-photo" role="img" aria-label="Preserved red roses in crystal blocks"></div>
  <p class="abs script preserved-label">Preserved Flowers</p>

  <div class="abs grid-orchid" role="img" aria-label="Pink orchid branch"></div>
  <div class="abs floral-lineart" role="img" aria-label="Faint lilac floral line art"></div>
  <div class="abs brand-mark"><span class="dot"></span>Bloom Velara</div>

  <div class="abs roses-photo" role="img" aria-label="Gold rose in gift box"></div>
  <p class="abs script roses-label">Roses</p>
  <div class="abs domes-photo" role="img" aria-label="Red roses under glass domes"></div>
  <p class="abs script projects-label">Preserved Projects</p>

  <div class="abs gifts-photo" role="img" aria-label="Red roses in black vases"></div>
  <p class="abs script gifts-label">Gifts for Occasions</p>

  <svg class="abs" style="left:361px;top:367px" width="352" height="352" viewBox="0 0 352 352">
    <circle cx="176" cy="176" r="168" fill="#5725a9"/>
  </svg>
  <div class="abs mission-text">
    <p class="green">Helping</p>
    <p class="white">Nature's Beauty</p>
    <p class="yellow">Last Forever</p>
    <p class="tag">#momentsfrozenintime</p>
  </div>
  <div class="abs gold-leaves" role="img" aria-label="Gold leaf sprigs"></div>

  <div class="abs wreath" role="img" aria-label="Yellow and peach rose wreath"></div>
  <div class="abs since">
    <p class="label">SINCE</p>
    <p class="num top">20</p>
    <p class="num bottom">05</p>
  </div>
</section>

</body>
</html>
```